Business card for Chiropractic clinics needs reworked / redesigned

The business card in attachment was designed 10 years ago. It is in need of an update.
We have 2 clinics:
VELDHOVE KLINIEK & VELDHOVE KLINIEK NOORD
Only one address needs to be on the card for doctors that only work in one clinic and two addresses need to be on the card for the doctors that work in both clinics.

Target Market(s)

patients/referrers

Industry/Entity Type

Medical

Contact Information for Business Card

Logo (in full or zoomed-in)
Clinic Name
Doctor name and title
clinic address, website, tel, email

Font styles to use
Sans Serif

Colors

Designer to choose colors to be used in the design.

Requirements
Must have
• Good contrast/readability
• We like modern minimalistic designs
• The Bcard needs to project our very high standard of proficiency/professionalism
Should not have
• Not curly
• Not to much colours

```html
<!DOCTYPE html>
<html lang="nl">
<head>
<meta charset="utf-8">
<title>Veldhove Kliniek – visitekaartje</title>
<link rel="stylesheet" href="https://fonts.googleapis.com/css2?family=Oswald:wght@300;500;600&family=Lato:wght@400;700&display=swap">
<style>
  :root {
    --backdrop: #2e5a49;
    --card-green: #1f5840;
    --card-white: #f4f4f2;
    --ink-green: #1d4f39;
    --soft-green: #7fa391;
    --muted-on-green: rgba(255,255,255,0.22);
    --white: #ffffff;
  }
  * { box-sizing: border-box; margin: 0; padding: 0; }
  html, body {
    width: 1200px; height: 1200px; overflow: hidden;
    background: var(--backdrop);
  }
  .sheet {
    width: 1200px; height: 1200px;
    display: flex; flex-direction: column; align-items: center; justify-content: center;
    gap: 60px;
  }
  .card {
    width: 840px; height: 480px; position: relative;
    box-shadow: 0 18px 40px rgba(0,0,0,0.25);
  }
  /* Front */
  .card--front { background: var(--card-green); }
  .clinic-names {
    position: absolute; left: 70px; top: 70px;
    padding-left: 22px; border-left: 2px solid var(--white);
    font-family: "Oswald", sans-serif; font-weight: 500;
    text-transform: uppercase; letter-spacing: 1px; line-height: 1.05;
  }
  .clinic-names__primary { color: var(--white); font-size: 52px; }
  .clinic-names__secondary { color: var(--muted-on-green); font-size: 52px; }
  /* Back */
  .card--back { background: var(--card-white); }
  .identity {
    position: absolute; left: 300px; top: 90px;
    font-family: "Oswald", sans-serif; color: var(--ink-green);
  }
  .identity__name {
    font-size: 44px; font-weight: 600; letter-spacing: 7px; text-transform: uppercase;
  }
  .identity__title {
    font-size: 22px; font-weight: 300; letter-spacing: 6px; text-transform: uppercase;
    color: var(--soft-green); margin-top: 2px; padding-left: 50px;
  }
  .locations {
    position: absolute; left: 220px; top: 250px;
    display: flex; align-items: stretch;
    font-family: "Lato", sans-serif; font-size: 19px; line-height: 1.3;
    color: var(--ink-green); text-transform: uppercase; letter-spacing: 1px;
  }
  .location { padding: 4px 24px; }
  .location--first { text-align: right; border-right: 2px solid var(--ink-green); }
  .location--second { padding-top: 50px; }
</style>
</head>
<body>
<main class="sheet">
  <section class="card card--front" aria-label="Voorkant visitekaartje">
    <h1 class="clinic-names">
      <span class="clinic-names__primary">Veldhove Kliniek</span><br>
      <span class="clinic-names__secondary">Veldhove Kliniek Noord</span>
    </h1>
  </section>

  <section class="card card--back" aria-label="Achterkant visitekaartje">
    <div class="identity">
      <p class="identity__name">Maarten Verlinden</p>
      <p class="identity__title">Chiropractor</p>
    </div>
    <div class="locations">
      <address class="location location--first">
        Veldhove Kliniek<br>
        Lindendreef 48<br>
        09 000 14 20<br>
        veldhovekliniek.be
      </address>
      <address class="location location--second">
        Veldhove Kliniek Noord<br>
        Kerkstraat 17<br>
        09 000 58 31<br>
        veldhovenoord.be
      </address>
    </div>
  </section>
</main>
</body>
</html>
```